Business Card Design Project

Business card design using our logo, consistent with website branding (www.brightvane.com.au) and includes our services:

advertising|sales|events|production

Details Required:

Dorian Webb
Managing Director

P 1300 586 231
M 0404 827 659
F (02) 9613 2048
E dorian@brightvane.com.au
W www.brightvane.com.au

Will be printed on high quality card with rounded corners.

Quick turnaround required, on standby for any questions to assist with this.

Will upload logo and previous drafts we didn't think were the right fit.

Target Market(s)

Senior business decision-makers

Industry/Entity Type

Business

Requirements
Must have
• Editable template, so details can be updated for staff

Must be in print ready format - please see specs I have just uploaded

```html
<!DOCTYPE html>
<html lang="en">
<head>
<meta charset="utf-8">
<title>BrightVane Business Card</title>
<link rel="stylesheet" href="https://fonts.googleapis.com/css2?family=Questrial&family=Arimo:wght@400;700&display=swap">
<style>
  :root {
    --bg-light: #f3f3f4;
    --bg-edge: #cbccce;
    --band: #d5d6d8;
    --ink: #2b2b2e;
    --label: #4d5c78;
    --divider: #050505;
    --pill-deep: #1672b8;
    --pill-bright: #27a6df;
    --mark: #1f7fc4;
    --white: #ffffff;
  }
  * { margin: 0; padding: 0; box-sizing: border-box; }
  html, body { width: 1051px; height: 1200px; overflow: hidden; }
  body { position: relative; background: var(--bg-edge); font-family: "Arimo", Arial, sans-serif; }

  .card-side { position: absolute; left: 0; width: 1051px; }
  .card-front { top: 0; height: 595px; background: radial-gradient(ellipse 60% 55% at 50% 48%, var(--bg-light), var(--bg-edge)); }
  .card-back { top: 601px; height: 599px; background: radial-gradient(ellipse 60% 60% at 50% 45%, var(--bg-light), var(--bg-edge)); }
  .side-divider { position: absolute; left: 0; top: 595px; width: 1051px; height: 5px; background: var(--divider); }

  .logo-band { position: absolute; left: 110px; top: 138px; width: 830px; height: 252px; background: var(--band); }

  .brand { position: absolute; display: flex; align-items: center; gap: 26px; }
  .brand-dot { width: 150px; height: 150px; border-radius: 50%; background: var(--mark); flex: none; }
  .brand-name { font-family: "Questrial", "Century Gothic", sans-serif; font-size: 74px; color: var(--ink); letter-spacing: -1px; line-height: 1; }
  .front-brand { left: 250px; top: 188px; }

  .pill {
    position: absolute; left: 271px; width: 509px; height: 67px; border-radius: 8px;
    padding: 0 10px;
    background: linear-gradient(90deg, var(--pill-deep), var(--pill-bright) 50%, var(--pill-deep));
    color: var(--white); display: flex; align-items: center; justify-content: center;
    font-size: 28px; white-space: nowrap; overflow: hidden;
  }
  .services { top: 421px; padding: 0 4px; }
  .sep { margin: 0 8px; }

  .back-mark { position: absolute; left: 460px; top: 50px; width: 130px; height: 130px; border-radius: 50%; background: var(--mark); }
  .back-name { position: absolute; left: 0; width: 1051px; top: 200px; text-align: center; font-family: "Questrial", "Century Gothic", sans-serif; font-size: 40px; line-height: 1; color: var(--ink); }

  .title-pill { top: 275px; font-size: 30px; }
  .title-pill .sep { margin: 0 7px; }
  .person { font-weight: 700; }
  .role { font-weight: 400; }

  .contacts { position: absolute; left: 0; top: 364px; width: 1051px; text-align: center; list-style: none; font-size: 35px; line-height: 37.5px; color: var(--ink); }
  .contacts .label { color: var(--label); margin-right: 6px; }
</style>
</head>
<body>
  <section class="card-side card-front">
    <div class="logo-band"></div>
    <div class="brand front-brand">
      <span class="brand-dot"></span>
      <span class="brand-name">BrightVane</span>
    </div>
    <div class="pill services">
      Advertising<span class="sep">|</span>Sales<span class="sep">|</span>Events<span class="sep">|</span>Production
    </div>
  </section>

  <div class="side-divider"></div>

  <section class="card-side card-back">
    <span class="back-mark"></span>
    <div class="back-name">BrightVane</div>
    <div class="pill title-pill">
      <span class="person">Dorian Webb</span><span class="person sep">|</span><span class="role">Managing Director</span>
    </div>
    <ul class="contacts">
      <li><span class="label">P</span>1300 586 231</li>
      <li><span class="label">M</span>0404 827 659</li>
      <li><span class="label">F</span>(02) 9613 2048</li>
      <li><span class="label">E</span>dorian@brightvane.com.au</li>
      <li><span class="label">W</span>www.brightvane.com.au</li>
    </ul>
  </section>
</body>
</html>
```